Selka Marrow Photography Business Card

I need a new business card/ possibly design to use for other marking materials ... I have included my logo below in a few different colors, but can also provide the logo in additional colors and sizes. I would love a card the expresses clean, simple and classy.

Target Market(s)

Portrait photography clients, child photography clients

Industry/Entity Type

Photographer

Contact Information for Business Card

Selka Marrow Photography, Fernhollow MA, www.selkamarrowphotography.example
T. 555-283-9146 E. selkamarrowphoto@mailbox.example

Colors
33b8a4
eea4c8
5c5c5c

Requirements
Must have
• I would like to include my logo on card.
Nice to have
• I also like the color brown as well as the choices below. I would like a simple, elegant card, something classy.

```html
<!DOCTYPE html>
<html lang="en">
<head>
<meta charset="utf-8">
<title>Selka Marrow Photography – Business Card</title>
<link rel="stylesheet" href="https://fonts.googleapis.com/css2?family=Questrial&display=swap">
<style>
  :root {
    --teal: #53b8b0;
    --white: #ffffff;
    --page: #ffffff;
    --card-edge: #e4e4e4;
  }
  html, body {
    margin: 0;
    padding: 0;
    overflow: hidden;
  }
  body {
    width: 1200px;
    height: 807px;
    background: var(--page);
    position: relative;
    font-family: "Questrial", sans-serif;
  }
  .card {
    position: absolute;
    left: 378px;
    width: 468px;
    height: 262px;
    box-sizing: border-box;
  }
  .card--front {
    top: 111px;
    background: var(--teal);
    color: var(--white);
  }
  .card--back {
    top: 447px;
    background: var(--white);
    color: var(--teal);
    border: 1px solid var(--card-edge);
  }
  .brand {
    position: absolute;
    left: 0;
    right: 0;
    text-align: center;
    margin: 0;
    font-weight: 400;
  }
  .brand__name {
    display: block;
    letter-spacing: 0.5px;
  }
  .brand__trade {
    display: block;
    text-transform: uppercase;
  }
  .card--front .brand { top: 84px; }
  .card--front .brand__name { font-size: 34px; line-height: 40px; }
  .card--front .brand__trade { font-size: 13px; letter-spacing: 6.5px; margin-top: 20px; }

  .card--back .brand { top: 40px; }
  .card--back .brand__name { font-size: 22px; line-height: 26px; }
  .card--back .brand__trade { font-size: 8.5px; letter-spacing: 4px; margin-top: 10px; }

  .frame {
    position: absolute;
    inset: 0;
  }
  .corner-flourish {
    position: absolute;
    top: 6px;
    width: 34px;
    height: 38px;
    background: linear-gradient(135deg, rgba(83,184,176,0.35), rgba(83,184,176,0.12));
    border-radius: 40% 40% 50% 50%;
  }
  .corner-flourish--left { left: 6px; }
  .corner-flourish--right { right: 6px; }

  .contact {
    position: absolute;
    left: 0;
    right: 0;
    top: 112px;
    margin: 0;
    text-align: center;
    font-size: 15.5px;
    line-height: 22px;
    font-style: normal;
  }
  .contact__city { display: block; margin-bottom: 15px; }
  .contact__web, .contact__mail { display: block; }
  .contact__phone { display: block; margin-top: 17px; }
</style>
</head>
<body>
  <section class="card card--front" aria-label="Business card front">
    <h1 class="brand">
      <span class="brand__name">Selka Marrow</span>
      <span class="brand__trade">Photography</span>
    </h1>
  </section>

  <section class="card card--back" aria-label="Business card back">
    <svg class="frame" width="466" height="260" viewBox="0 0 466 260" aria-hidden="true">
      <rect x="16" y="16" width="434" height="230" fill="none" stroke="var(--teal)" stroke-width="1.5"/>
    </svg>
    <div class="corner-flourish corner-flourish--left" role="img" aria-label="Curling swirl ornament at top-left corner"></div>
    <div class="corner-flourish corner-flourish--right" role="img" aria-label="Curling swirl ornament at top-right corner"></div>

    <h2 class="brand">
      <span class="brand__name">Selka Marrow</span>
      <span class="brand__trade">Photography</span>
    </h2>

    <address class="contact">
      <span class="contact__city">Fernhollow MA</span>
      <span class="contact__web">www.selkamarrowphotography.example</span>
      <span class="contact__mail">selkamarrowphoto@mailbox.example</span>
      <span class="contact__phone">555-283-9146</span>
    </address>
  </section>
</body>
</html>
```